Bramblecourt Partners Needs a Graphic Image

We need an image to use on our new website as well as on Facebook and Linked In. The image should be 860x450 pixels and creatively use four colors: black, gold, gray, and white. The image design should focus on a "bank check." The amount of the check should be for $1 million. It should be made out to "Your Social-Purpose Organization." It should come from a hypothetical organization called The Social Investment Fund with an address of 1234 Bramblecourt Place, Anywhere, USA. It should be signed by the CEO of The Social Investment Fund. In the "comments area" of the check, it should read "Funding for Yr. 1 of Your Growth Capital Plan."

The organization and website you'll be creating this graphic for is called Bramblecourt Partners LLC. We provide solutions that enable social purpose organizations to get the growth capital funding they need to turn their vision of the future into reality.

```html
<!DOCTYPE html>
<html lang="en">
<head>
<meta charset="utf-8">
<title>Growth Capital Check</title>
<link rel="stylesheet" href="https://fonts.googleapis.com/css2?family=PT+Sans&family=Caveat:wght@500&display=swap">
<style>
  :root {
    --backdrop: #e7e2d8;
    --paper: #f1eee6;
    --paper-shade: #e6e2d7;
    --gold: #b59a55;
    --gold-dark: #8f7738;
    --ink: #1e1e1e;
    --print: #2b2b2b;
    --rule: #4a4a4a;
    --box: #ffffff;
  }
  html, body {
    margin: 0;
    width: 1200px;
    height: 628px;
    overflow: hidden;
    background: var(--backdrop);
  }
  .canvas {
    position: relative;
    width: 1200px;
    height: 628px;
  }
  .check {
    position: absolute;
    left: 130px;
    top: 94px;
    width: 940px;
    height: 440px;
    background: linear-gradient(180deg, var(--paper) 0%, var(--paper-shade) 100%);
    box-shadow: 0 6px 18px rgba(0,0,0,0.18);
  }
  .check-frame {
    position: absolute;
    inset: 0;
  }
  .printed {
    position: absolute;
    font-family: "PT Sans", sans-serif;
    color: var(--print);
    white-space: nowrap;
  }
  .issuer {
    left: 64px;
    top: 62px;
    font-size: 17px;
    line-height: 22px;
  }
  .label {
    font-size: 13px;
    letter-spacing: 0.3px;
    line-height: 15px;
  }
  .label-date { left: 610px; top: 98px; }
  .label-payee { left: 64px; top: 176px; }
  .label-dollar { left: 614px; top: 166px; font-size: 15px; }
  .label-dollars { left: 812px; top: 248px; }
  .label-memo { left: 64px; top: 352px; }
  .written {
    position: absolute;
    font-family: "Caveat", cursive;
    color: var(--ink);
    white-space: nowrap;
    line-height: 1;
  }
  .date-value { left: 680px; top: 74px; font-size: 32px; }
  .payee-value { left: 160px; top: 160px; font-size: 34px; }
  .words-value { left: 74px; top: 228px; font-size: 34px; }
  .memo-value { left: 110px; top: 334px; font-size: 30px; }
  .signature { left: 624px; top: 306px; font-size: 34px; }
  .rule {
    position: absolute;
    height: 1.5px;
    background: var(--rule);
  }
  .rule-date { left: 664px; top: 110px; width: 180px; }
  .rule-payee { left: 150px; top: 196px; width: 442px; }
  .rule-words { left: 64px; top: 264px; width: 736px; }
  .rule-memo { left: 104px; top: 366px; width: 486px; }
  .rule-sign { left: 614px; top: 346px; width: 256px; }
  .amount-box {
    position: absolute;
    left: 632px;
    top: 140px;
    width: 194px;
    height: 46px;
    background: var(--box);
    font-family: "Caveat", cursive;
    font-size: 34px;
    color: var(--ink);
    line-height: 46px;
    text-align: center;
    white-space: nowrap;
  }
  .micr {
    position: absolute;
    left: 80px;
    top: 392px;
    font-family: "PT Sans", sans-serif;
    font-size: 20px;
    letter-spacing: 4px;
    color: var(--print);
    white-space: nowrap;
  }
</style>
</head>
<body>
<main class="canvas">
  <section class="check" aria-label="Check for one million dollars">
    <svg class="check-frame" width="940" height="440" viewBox="0 0 940 440">
      <rect x="14" y="14" width="912" height="412" fill="none" stroke="var(--gold)" stroke-width="3"/>
      <rect x="22" y="22" width="896" height="396" fill="none" stroke="var(--gold)" stroke-width="1"/>
      <g fill="var(--gold-dark)" role="img" aria-label="Corner flourishes">
        <rect x="8" y="8" width="22" height="22"/>
        <rect x="910" y="8" width="22" height="22"/>
        <rect x="8" y="410" width="22" height="22"/>
        <rect x="910" y="410" width="22" height="22"/>
      </g>
    </svg>

    <div class="printed issuer">The Social Investment Fund<br>1234 Bramblecourt Place<br>New York City, New York, USA</div>

    <div class="printed label label-date">DATE</div>
    <div class="written date-value">TBD</div>
    <div class="rule rule-date"></div>

    <div class="printed label label-payee">PAY TO THE<br>ORDER OF</div>
    <div class="written payee-value">Your Social Purpose Organization</div>
    <div class="rule rule-payee"></div>

    <div class="printed label-dollar">$</div>
    <div class="amount-box">1,000,000.00</div>

    <div class="written words-value">One million dollars and zero cents</div>
    <div class="rule rule-words"></div>
    <div class="printed label label-dollars">DOLLARS</div>

    <div class="printed label label-memo">MEMO</div>
    <div class="written memo-value">Funding for Yr. 1 of Growth Capital Plan</div>
    <div class="rule rule-memo"></div>

    <div class="written signature">Dana Whitfield, CEO</div>
    <div class="rule rule-sign"></div>

    <div class="micr">⑆123456789⑆1234 &nbsp; 123456789⑈</div>
  </section>
</main>
</body>
</html>
```